Marchesi Orthodontics
Business Card / Stationary Design
Professional
Lucia Marchesi
Orthodontist
4817 W. Harborview Ave. Suite 204
Fort Lauderdale, FL 33419
marchesiortho@mailvexo.com
www.pinegrovesmiles.com

```html
<!DOCTYPE html>
<html lang="en">
<head>
<meta charset="utf-8">
<title>Marchesi Orthodontics – Stationery Set</title>
<link href="https://fonts.googleapis.com/css2?family=Exo+2:wght@600;700&family=Open+Sans:wght@400;600&display=swap" rel="stylesheet">
<style>
  :root {
    --blue: #1a7fd0;
    --blue-dark: #0d5ea8;
    --blue-light: #7cc8f2;
    --ice: #e6f3fb;
    --grey: #9ea4aa;
    --grey-dark: #6f767c;
    --paper: #ffffff;
    --ink: #4a4f55;
    --backdrop: #eef0f2;
  }
  * { box-sizing: border-box; margin: 0; padding: 0; }
  html, body { width: 1200px; height: 650px; overflow: hidden; }
  body { background: var(--backdrop); font-family: "Open Sans", sans-serif; color: var(--ink); position: relative; }
  .piece { position: absolute; background: var(--paper); box-shadow: 0 2px 6px rgba(0,0,0,.18); overflow: hidden; }
  .piece svg.swoosh { position: absolute; left: 0; top: 0; width: 100%; height: 100%; }
  .wordmark { font-family: "Exo 2", sans-serif; font-weight: 700; color: var(--blue); letter-spacing: .08em; line-height: 1; position: absolute; }
  .wordmark span { display: block; font-size: .42em; letter-spacing: .28em; margin-top: .25em; }
  .wordmark.on-blue { color: var(--paper); }
  .small { font-size: 5px; line-height: 1.5; position: absolute; }
  .small.white { color: var(--paper); }

  /* business cards */
  .card { top: 19px; width: 156px; height: 89px; }
  .card-front-name { left: 12px; }
  .card-contact { left: 173px; }
  .card-blue { left: 343px; background: linear-gradient(135deg, var(--blue-light), var(--blue) 55%, var(--blue-dark)); }
  .card-reminder { left: 514px; width: 158px; }
  .person { position: absolute; right: 10px; top: 10px; text-align: right; }
  .person b { display: block; font-size: 6.5px; color: var(--blue-dark); }
  .person i { font-style: normal; font-size: 5px; }
  .slot { position: absolute; height: 6px; border-bottom: .6px solid var(--grey); width: 26px; }

  /* envelopes */
  .envelope-front { left: 24px; top: 137px; width: 372px; height: 146px; }
  .envelope-backs { left: 24px; top: 293px; width: 372px; height: 336px; background: none; box-shadow: none; }
  .flap { position: absolute; left: 0; width: 372px; }

  /* letterhead & fax */
  .sheet { top: 106px; width: 354px; height: 523px; }
  .letterhead { left: 427px; }
  .fax { left: 816px; }
  .fax-band { position: absolute; left: 10px; right: 10px; top: 88px; height: 22px; background: linear-gradient(90deg, var(--ice), var(--blue) 70%, var(--blue-dark)); }
  .fax-title { position: absolute; right: 14px; top: 5px; color: var(--paper); font-family: "Exo 2", sans-serif; font-weight: 700; font-size: 11px; letter-spacing: .1em; }
  .fax-title::before { content: ""; display: inline-block; width: 14px; height: 0; border-top: 2px solid var(--paper); margin-right: 6px; vertical-align: middle; }
  .pill { position: absolute; left: 14px; width: 22px; height: 10px; border-radius: 3px; background: var(--blue); color: var(--paper); font-size: 4.5px; text-align: center; line-height: 10px; }
  .field { position: absolute; left: 58px; width: 210px; font-size: 5px; border-bottom: .6px solid #c9ced3; height: 9px; }
  .field b { display: inline-block; width: 34px; font-weight: 600; text-align: right; margin-right: 6px; }
  .fax-box { position: absolute; left: 58px; top: 236px; width: 268px; height: 150px; border: .8px solid #c9ced3; }
</style>
</head>
<body>

<!-- Business card: name side -->
<div class="piece card card-front-name">
  <svg class="swoosh" viewBox="0 0 156 89" preserveAspectRatio="none" aria-hidden="true">
    <path d="M0 0 H38 C20 30 30 65 70 89 H0 Z" fill="var(--blue)"/>
    <path d="M38 0 C24 30 34 66 76 89 H70 C30 65 20 30 38 0 Z" fill="var(--blue-light)"/>
  </svg>
  <div class="person"><b>Lucia Marchesi</b><i>Orthodontist</i></div>
  <div class="wordmark" style="left:66px;top:44px;font-size:10px;">MARCHESI<span>ORTHODONTICS</span></div>
</div>

<!-- Business card: contact side -->
<div class="piece card card-contact">
  <svg class="swoosh" viewBox="0 0 156 89" preserveAspectRatio="none" aria-hidden="true">
    <path d="M0 70 C50 58 100 74 156 60 V89 H0 Z" fill="var(--blue)"/>
    <path d="M0 66 C50 54 100 70 156 56 V60 C100 74 50 58 0 70 Z" fill="var(--blue-light)"/>
  </svg>
  <div class="wordmark" style="left:28px;top:10px;font-size:10px;">MARCHESI<span>ORTHODONTICS</span></div>
  <div class="small" style="left:28px;top:36px;">4817 W. Harborview Ave. Suite 204<br>Fort Lauderdale, FL 33419<br>Tel 954.555.0147<br>marchesiortho@mailvexo.com</div>
  <div class="small white" style="left:46px;top:76px;">www.pinegrovesmiles.com</div>
</div>

<!-- Business card: blue side -->
<div class="piece card card-blue">
  <div class="wordmark on-blue" style="left:36px;top:30px;font-size:11px;">MARCHESI<span>ORTHODONTICS</span></div>
  <div class="small white" style="left:46px;top:70px;">www.pinegrovesmiles.com</div>
</div>

<!-- Business card: appointment reminder -->
<div class="piece card card-reminder">
  <div class="wordmark" style="left:36px;top:8px;font-size:10px;">MARCHESI<span>ORTHODONTICS</span></div>
  <div class="small" style="left:48px;top:32px;font-weight:600;color:var(--blue-dark);">Your next appointment</div>
  <div class="slot" style="left:22px;top:46px;"></div><div class="slot" style="left:52px;top:46px;"></div>
  <div class="slot" style="left:82px;top:46px;"></div><div class="slot" style="left:112px;top:46px;"></div>
  <div class="small" style="left:40px;top:58px;">Date ________ &nbsp; Time ______</div>
  <div class="small" style="left:46px;top:74px;color:var(--blue);">www.pinegrovesmiles.com</div>
</div>

<!-- Envelope front -->
<div class="piece envelope-front">
  <svg class="swoosh" viewBox="0 0 372 146" preserveAspectRatio="none" aria-hidden="true">
    <path d="M150 146 C230 120 300 100 372 70 V146 Z" fill="var(--blue)"/>
    <path d="M140 146 C225 116 298 94 372 62 V70 C300 100 230 120 150 146 Z" fill="var(--grey)"/>
  </svg>
  <div class="wordmark" style="left:12px;top:12px;font-size:12px;">MARCHESI<span>ORTHODONTICS</span></div>
  <div class="small" style="left:236px;top:62px;">4817 W. Harborview Ave. Suite 204<br>Fort Lauderdale, FL 33419</div>
  <div class="small white" style="left:290px;top:104px;">Tel 954.555.0147<br>marchesiortho@mailvexo.com<br>www.pinegrovesmiles.com</div>
</div>

<!-- Envelope backs -->
<div class="piece envelope-backs">
  <svg class="flap" style="top:0;height:120px;" viewBox="0 0 372 120" preserveAspectRatio="none" aria-hidden="true">
    <rect width="372" height="120" fill="var(--paper)"/>
    <path d="M0 0 H372 L186 60 Z" fill="#f6f7f8" stroke="#d8dcdf" stroke-width=".8"/>
  </svg>
  <svg class="flap" style="top:92px;height:130px;" viewBox="0 0 372 130" preserveAspectRatio="none" aria-hidden="true">
    <defs><linearGradient id="flapBlue" x1="0" x2="0" y1="0" y2="1"><stop offset="0" stop-color="var(--blue-light)"/><stop offset=".6" stop-color="var(--blue)"/><stop offset="1" stop-color="var(--blue-dark)"/></linearGradient></defs>
    <rect y="20" width="372" height="110" fill="var(--paper)"/>
    <path d="M0 0 H372 V20 L186 70 L0 20 Z" fill="url(#flapBlue)"/>
  </svg>
  <svg class="flap" style="top:196px;height:140px;" viewBox="0 0 372 140" preserveAspectRatio="none" aria-hidden="true">
    <defs><linearGradient id="flapGrey" x1="0" x2="0" y1="0" y2="1"><stop offset="0" stop-color="#d9dcdf"/><stop offset=".6" stop-color="var(--grey)"/><stop offset="1" stop-color="var(--grey-dark)"/></linearGradient></defs>
    <rect y="20" width="372" height="120" fill="var(--paper)"/>
    <path d="M0 0 H372 V20 L186 70 L0 20 Z" fill="url(#flapGrey)"/>
  </svg>
</div>

<!-- Letterhead -->
<div class="piece sheet letterhead">
  <svg class="swoosh" viewBox="0 0 354 523" preserveAspectRatio="none" aria-hidden="true">
    <path d="M150 523 C240 490 300 450 354 400 V523 Z" fill="var(--blue)"/>
    <path d="M140 523 C236 484 298 442 354 392 V400 C300 450 240 490 150 523 Z" fill="var(--grey)"/>
  </svg>
  <div class="wordmark" style="left:14px;top:18px;font-size:13px;">MARCHESI<span>ORTHODONTICS</span></div>
  <div class="small white" style="left:248px;top:470px;">4817 W. Harborview Ave. Suite 204<br>Fort Lauderdale, FL 33419<br>Tel 954.555.0147<br>www.pinegrovesmiles.com</div>
</div>

<!-- Fax cover -->
<div class="piece sheet fax">
  <svg class="swoosh" viewBox="0 0 355 523" preserveAspectRatio="none" aria-hidden="true">
    <path d="M150 523 C240 490 300 450 355 400 V523 Z" fill="var(--blue)"/>
    <path d="M140 523 C236 484 298 442 355 392 V400 C300 450 240 490 150 523 Z" fill="var(--grey)"/>
  </svg>
  <div class="wordmark" style="left:14px;top:18px;font-size:13px;">MARCHESI<span>ORTHODONTICS</span></div>
  <div class="fax-band"><div class="fax-title">FAX</div></div>
  <div class="pill" style="top:122px;">Urgent</div>
  <div class="pill" style="top:170px;">Review</div>
  <div class="pill" style="top:202px;">Reply</div>
  <div class="field" style="top:122px;"><b>To</b></div>
  <div class="field" style="top:136px;"><b>From</b></div>
  <div class="field" style="top:150px;"><b>Date</b></div>
  <div class="field" style="top:164px;"><b>Fax</b></div>
  <div class="field" style="top:178px;"><b>Phone</b></div>
  <div class="field" style="top:192px;"><b>Pages</b></div>
  <div class="field" style="top:206px;"><b>Re</b></div>
  <div class="fax-box"></div>
  <div class="small white" style="left:248px;top:470px;">4817 W. Harborview Ave. Suite 204<br>Fort Lauderdale, FL 33419<br>Fax 954.555.0148<br>www.pinegrovesmiles.com</div>
</div>

</body>
</html>
```